Award winning photographer needs a website.

I need a Wordpress website that showcases my photos. I want them arranged via category, which might be a specific place or a theme. Here are categories I am thinking of:
1. Yarra Valley and Ranges
2. East coast Tasmania
3. Landscapes
4. Seascapes
5. Urban
6. Nepal
7. Macro
I need to be able to upload and download the photos myself. Currently, there is no need for this site to have an ecommerce component. I would like a blog page where I can post about my photographic adventures and maybe add some short videos of me on my way to the shoot, or of the people I meet. I also want to have it so that each photo has a title and if people click on a photo they can read a story about how I came to shoot it etc. There will also be my contact details and how to purchase a print which will happen through other communications. Like i mentioned, no e commerce at this point. I would like a page for awards as I have several. Here are some URLs of sites I like to give you some idea of what I'm looking at:

https://www.maplundra.com/
https://brontefaulkphotography.com/
https://www.mariodevinephotography.com/

I can upload some images for you to start putting together someting if that hepls

Industry/Entity Type

Photography

Coding

Coded - Design and coding required

Number of Pages Required

5+ page

Font styles to use
Sans Serif

Requirements
Must have
• Multiple pages to display photos in different categories

```html
<!DOCTYPE html>
<html lang="en">
<head>
<meta charset="utf-8">
<title>Daniel Ashworth Photography</title>
<link rel="stylesheet" href="https://fonts.googleapis.com/css2?family=Bebas+Neue&family=Montserrat:wght@400;500;600&family=Mrs+Saint+Delafield&display=swap">
<style>
:root{
  --ink:#111111;
  --text:#555555;
  --white:#ffffff;
  --red:#e52b2b;
  --dark-red:#b31d1d;
  --teal:#5f9ca2;
  --navy:#1f3447;
  --footer:#121212;
  --line:#d9d9d9;
  --muted:#9a9a9a;
}
*{box-sizing:border-box;margin:0;padding:0}
html,body{width:1200px;height:2843px;overflow:hidden;background:var(--white)}
body{font-family:"Montserrat",sans-serif;color:var(--text);position:relative}
.abs{position:absolute}
.script{font-family:"Mrs Saint Delafield",cursive}
.display{font-family:"Bebas Neue",sans-serif;color:var(--white);letter-spacing:.5px}

/* header */
.site-header{left:0;top:0;width:1200px;height:103px;border-bottom:1px solid var(--line)}
.brand{left:30px;top:38px;font-size:22px;font-weight:500;color:var(--ink);letter-spacing:1px}
.main-nav{left:530px;top:45px;display:flex;gap:31px;font-size:13px;color:#333;white-space:nowrap}
.social{display:flex;gap:16px}
.social span{width:20px;height:20px;border-radius:50%;background:var(--ink);display:block}
.header-social{left:1072px;top:43px}

/* hero grid */
.tile{overflow:hidden}
.tile .label{position:absolute;left:19px;font-family:"Bebas Neue",sans-serif;color:var(--white);font-size:30px;line-height:1}
.tile p{position:absolute;left:19px;color:var(--white);font-size:13.5px;line-height:21px;width:280px}
.yarra{left:0;top:103px;width:502px;height:650px;background:linear-gradient(160deg,#6f7a2a 0%,#4c5a1d 35%,#8c7a2c 60%,#3d3a16 100%)}
.tasmania{left:502px;top:103px;width:349px;height:309px;background:linear-gradient(180deg,#c2395a 0%,#d3485a 45%,#5b2a22 70%,#8a3b2c 100%)}
.landscapes{left:502px;top:412px;width:349px;height:125px;background:linear-gradient(180deg,#3a5372 0%,#d889a6 40%,#9cc7d3 75%,#3e5a70 100%)}
.seascapes{left:502px;top:537px;width:349px;height:216px;background:linear-gradient(180deg,#2f3346 0%,#c56a34 45%,#e6913b 55%,#352b3c 100%)}
.nepal{left:851px;top:103px;width:349px;height:217px;background:linear-gradient(170deg,#58565a 0%,#8f8170 40%,#2e3341 75%,#1d2530 100%)}
.urban{left:851px;top:320px;width:349px;height:217px;background:linear-gradient(180deg,#141a24 0%,#1f2833 50%,#6b5a2e 75%,#151512 100%)}
.macro{left:851px;top:537px;width:349px;height:216px;background:radial-gradient(circle at 60% 45%,#e0387d 0%,#b9265f 25%,#0b0b0b 60%)}

/* about */
.portrait{left:127px;top:820px;width:158px;height:488px;background:linear-gradient(180deg,#e9e4e0 0%,#b58e78 22%,#355a80 50%,#2a4563 100%)}
.name-vertical{font-family:"Bebas Neue",sans-serif;writing-mode:vertical-rl;transform:rotate(180deg);line-height:.82;text-align:center}
.name-first{left:286px;top:803px;font-size:185px;color:var(--navy);height:505px}
.name-last{left:436px;top:830px;font-size:104px;color:var(--teal);height:478px}
.about-copy{left:593px;top:826px;width:485px;font-size:14.5px;line-height:22.5px;color:#666}
.about-copy p+p{margin-top:22.5px}
.signature{left:593px;top:1186px;width:360px;height:72px;background:linear-gradient(90deg,#f1f1f1,#e6e6e6)}
.btn-dark{left:971px;top:1206px;width:161px;height:43px;background:var(--ink);color:var(--white);font-size:14px;display:flex;align-items:center;justify-content:center}

/* blog */
.blog{left:0;top:1345px;width:1200px;height:775px;background:linear-gradient(180deg,#2c3150 0%,#5e5a7d 25%,#d7a0b8 48%,#7b6b8e 62%,#2f4d3a 75%,#3d5a2e 100%)}
.blog-badge{left:128px;top:1715px;width:88px;height:38px;background:var(--red);color:var(--white);font-family:"Bebas Neue",sans-serif;font-size:30px;text-align:center;line-height:40px}
.blog-title{left:124px;top:1763px;font-size:82px;line-height:92px}
.blog-excerpt{left:118px;top:1958px;width:380px;font-size:16px;line-height:22px;color:var(--white)}
.blog-link{left:120px;top:2013px;font-size:16px;color:var(--white);text-decoration:underline}
.video-card{left:596px;width:477px;height:203px;display:flex;align-items:center;justify-content:center;gap:30px}
.video-card .display{font-size:32px}
.card-1{top:1407px;background:linear-gradient(180deg,#5e7189 0%,#8fa0b1 55%,#6c5d47 80%,#3f3a31 100%)}
.card-2{top:1632px;background:linear-gradient(180deg,#566e8c 0%,#c2c8cf 35%,#b43a3a 65%,#2e4c7a 100%)}
.card-3{top:1857px;background:linear-gradient(180deg,#6a8ea8 0%,#d98a5d 55%,#c25a34 75%,#7b4a3a 100%)}
.play{width:40px;height:40px}

/* subscribe */
.subscribe{left:0;top:2120px;width:1200px;height:458px;background:linear-gradient(180deg,#fafafa 0%,#efefef 55%,#e4e4e4 100%)}
.subscribe-title{left:0;top:2160px;width:1200px;text-align:center;font-size:120px;color:#3a3a3a;line-height:1}
.subscribe-text{left:195px;top:2307px;width:810px;text-align:center;font-size:14.5px;line-height:22.5px;color:#555}
.signup{left:311px;top:2383px;width:578px;height:49px;display:flex;border:1px solid #333}
.signup-input{width:383px;background:var(--white)}
.signup-btn{flex:1;background:var(--ink);color:var(--red);font-size:14px;display:flex;align-items:center;justify-content:center}
.follow{left:458px;top:2470px;display:flex;align-items:center;gap:14px}
.follow-label{font-size:52px;color:#333}
.follow .social span{background:var(--dark-red)}

/* footer */
.site-footer{left:0;top:2578px;width:1200px;height:265px;background:var(--footer)}
.footer-brand{left:0;top:2660px;width:1200px;text-align:center;color:var(--dark-red);font-size:24px;font-weight:500;letter-spacing:1px}
.footer-nav{left:0;top:2737px;width:1200px;display:flex;justify-content:center;gap:40px;font-size:13px;color:var(--muted)}
.copyright{left:0;top:2772px;width:1200px;text-align:center;font-size:13px;color:var(--muted)}
</style>
</head>
<body>

<header class="site-header abs">
  <div class="brand abs">Daniel Ashworth</div>
  <nav class="main-nav abs">
    <span>HOME</span><span>GALLERY</span><span>BLOG</span><span>PHOTO TOURS</span><span>ABOUT ME</span><span>CONTACT</span>
  </nav>
  <div class="social header-social abs">
    <span role="img" aria-label="Social profile"></span>
    <span role="img" aria-label="Social profile"></span>
    <span role="img" aria-label="Video channel"></span>
  </div>
</header>

<section class="gallery-grid">
  <a class="tile yarra abs" role="img" aria-label="Golden light over a river winding through Yarra Valley forest">
    <div class="label" style="top:410px;font-size:56px;line-height:54px;left:30px">YARRA VALLEY<br>AND RANGES</div>
    <p style="top:520px;left:30px;width:330px;font-size:15px;line-height:25px">Lorem Ipsum is simply dummy text of the printing and typesetting industry. Lorem Ipsum has been the industry's</p>
  </a>
  <a class="tile tasmania abs" role="img" aria-label="Lone tree on red rocks under a pink Tasmanian sky">
    <div class="label" style="top:215px">EAST COAST TASMANIA</div>
    <p style="top:250px">Lorem Ipsum is simply dummy text of the printing and typesetting</p>
  </a>
  <a class="tile landscapes abs" role="img" aria-label="Coastal boulders at pastel sunset">
    <div class="label" style="top:75px">LANDSCAPES</div>
  </a>
  <a class="tile seascapes abs" role="img" aria-label="Jetty and boathouse at sunset over still water">
    <div class="label" style="top:158px">SEASCAPES</div>
  </a>
  <a class="tile nepal abs" role="img" aria-label="Misty Himalayan valley">
    <div class="label" style="top:172px;left:24px">NEPAL</div>
  </a>
  <a class="tile urban abs" role="img" aria-label="City skyline at night reflected on water">
    <div class="label" style="top:94px">URBAN</div>
    <p style="top:127px">Lorem Ipsum is simply dummy text of the printing and typesetting</p>
  </a>
  <a class="tile macro abs" role="img" aria-label="Close-up of a pink flower on black">
    <div class="label" style="top:158px;left:24px">MACRO</div>
  </a>
</section>

<section class="about">
  <div class="portrait abs" role="img" aria-label="Portrait of the photographer with camera strap"></div>
  <div class="name-vertical name-first abs">DANIEL</div>
  <div class="name-vertical name-last abs">ASHWORTH</div>
  <div class="about-copy abs">
    <p>Contrary to popular belief, Lorem Ipsum is not simply random text. It has roots in a piece of classical Latin literature from 45 BC, making it over 2000 years old. Edwin Harlow, a Latin professor at Alder Hill College in Virginia, looked up one of the more obscure Latin words, consectetur, from a Lorem Ipsum passage, and going through the cites of the word in classical literature, discovered the undoubtable source.</p>
    <p>Lorem Ipsum comes from sections 1.10.32 and 1.10.33 of "de Finibus Bonorum et Malorum" (The Extremes of Good and Evil) by Varrus, written in 45 BC. This book is a treatise on the theory of ethics, very popular during the Renaissance. The first line of Lorem Ipsum, "Lorem ipsum dolor sit amet..", comes from a line in section 1.10.32.</p>
  </div>
  <div class="signature abs" role="img" aria-label="Handwritten signature of the photographer"></div>
  <a class="btn-dark abs">Learn More</a>
</section>

<section class="blog abs" role="img" aria-label="Stormy pink sky with rainbow over green hills and a road"></section>
<div class="blog-badge abs">BLOG</div>
<h2 class="blog-title display abs">LPSUM QUIA<br>DOLOR</h2>
<p class="blog-excerpt abs">Neque porro quisquam est qui dolorem ipsum quia dolor sit amet, consectetur, adipisci velit...</p>
<a class="blog-link abs">Learn More &gt;</a>

<a class="video-card card-1 abs" role="img" aria-label="Clifftop village under a rainbow">
  <span class="display">LPSUM QUIA DOLOR</span>
  <svg class="play" viewBox="0 0 40 40"><circle cx="20" cy="20" r="20" fill="#111"/><path d="M15 12 L29 20 L15 28Z" fill="#fff"/></svg>
</a>
<a class="video-card card-2 abs" role="img" aria-label="Prayer flags before snowy mountain peaks">
  <span class="display">LPSUM QUIA DOLOR</span>
</a>
<a class="video-card card-3 abs" role="img" aria-label="Palm trees on a beach at sunset">
  <span class="display">LPSUM QUIA DOLOR</span>
  <svg class="play" viewBox="0 0 40 40"><circle cx="20" cy="20" r="20" fill="#c71f1f"/><path d="M15 12 L29 20 L15 28Z" fill="#fff"/></svg>
</a>

<section class="subscribe abs" role="img" aria-label="Faint misty mountain backdrop"></section>
<h2 class="subscribe-title script abs">Subscribe</h2>
<p class="subscribe-text abs">Lorem Ipsum is simply dummy text of the printing and typesetting industry. Lorem Ipsum has been the industry's standard dummy text ever since the 1500s, when an unknown printer.</p>
<form class="signup abs">
  <div class="signup-input"></div>
  <div class="signup-btn">SIGN UP</div>
</form>
<div class="follow abs">
  <span class="follow-label script">Follow Us:</span>
  <div class="social">
    <span role="img" aria-label="Social profile"></span>
    <span role="img" aria-label="Social profile"></span>
    <span role="img" aria-label="Video channel"></span>
  </div>
</div>

<footer class="site-footer abs"></footer>
<div class="footer-brand abs">D. Ashworth</div>
<nav class="footer-nav abs">
  <span>HOME</span><span>GALLERY</span><span>BLOG</span><span>PHOTO TOURS</span><span>ABOUT ME</span><span>CONTACT</span>
</nav>
<p class="copyright abs">Copyright © Daniel Ashworth Photography 2023 All Rights Reserved</p>

</body>
</html>
```